Life Coach for Lawyers Business Card Design

Elegant, original, business card design for life coaching service for associate attorneys who work in big law and struggle with stress, overwhelm, and time management. Double sided design.

Target Market(s)

Women associate attorneys who work in big law and struggle with stress, overwhelm, and time management.

Industry/Entity Type

Life Coaching

Contact Information for Business Card

Marissa Pendrell
Life Coach
518.677.3941
calmbriefcounsel.net
marissa@calmbriefcounsel.net
@calmbriefcounsel (Instagram)

Font styles to use
Other font styles liked:
• Silver South font duo. See uploaded files.

Requirements
Must have
• Icons for phone, website, email, and Instagram instead of words. Specific colors used in my logo (171B2B, 421121, FFFFFF)
Nice to have
• Foil. Embossed. Feminine design.
Should not have
• Any colors other than those used in logo. See uploaded files.

```html
<!DOCTYPE html>
<html lang="en">
<head>
<meta charset="utf-8">
<title>Calm Brief Counsel – Business Card</title>
<link rel="stylesheet" href="https://fonts.googleapis.com/css2?family=Bodoni+Moda:wght@400&family=Arimo:wght@400&display=swap">
<style>
  :root {
    --navy: #171B2B;
    --wine: #421121;
    --white: #FFFFFF;
    --page: #FFFFFF;
    --shadow: rgba(0, 0, 0, 0.55);
  }
  * { box-sizing: border-box; margin: 0; padding: 0; }
  html, body {
    width: 1200px; height: 1200px; overflow: hidden;
    background: var(--page);
  }
  .canvas { position: relative; width: 1200px; height: 1200px; }
  .card {
    position: absolute; left: 250px; width: 706px; height: 434px;
    color: var(--white);
    box-shadow: 18px 16px 22px -4px var(--shadow);
  }
  .card--front { top: 142px; background: var(--navy); }
  .card--back { top: 627px; background: var(--wine); }

  .wordmark {
    position: absolute;
    font-family: "Bodoni Moda", "Times New Roman", serif;
    font-weight: 400;
    color: var(--white);
    text-align: center;
    line-height: 1;
  }
  .wordmark__top { display: block; letter-spacing: 0.18em; }
  .wordmark__main { display: block; letter-spacing: 0.02em; }

  .card--front .wordmark { left: 0; right: 0; top: 142px; }
  .card--front .wordmark__top { font-size: 38px; margin-bottom: 8px; }
  .card--front .wordmark__main { font-size: 92px; }

  .card--back .wordmark { left: 23px; width: 318px; top: 160px; }
  .card--back .wordmark__top { font-size: 25px; margin-bottom: 6px; }
  .card--back .wordmark__main { font-size: 62px; }

  .divider {
    position: absolute; left: 353px; top: 103px;
    width: 1.5px; height: 242px; background: var(--white);
  }
  .identity {
    position: absolute; right: 15px; top: 104px;
    font-family: "Arimo", Arial, sans-serif; text-align: right;
  }
  .identity__name { font-size: 38px; line-height: 46px; }
  .identity__role { font-size: 26px; line-height: 34px; }

  .contacts {
    position: absolute; left: 391px; top: 228px; list-style: none;
    font-family: "Arimo", Arial, sans-serif; font-size: 17.5px;
  }
  .contacts__item {
    display: flex; align-items: center; height: 30px; margin-bottom: 2px;
  }
  .contacts__icon { width: 22px; height: 22px; margin-right: 12px; flex: none; }
</style>
</head>
<body>
<main class="canvas">
  <section class="card card--front" aria-label="Card front">
    <div class="wordmark">
      <span class="wordmark__top">CALM BRIEF</span>
      <span class="wordmark__main">COUNSEL</span>
    </div>
  </section>

  <section class="card card--back" aria-label="Card back">
    <div class="wordmark">
      <span class="wordmark__top">CALM BRIEF</span>
      <span class="wordmark__main">COUNSEL</span>
    </div>
    <div class="divider"></div>
    <div class="identity">
      <p class="identity__name">Marissa Pendrell</p>
      <p class="identity__role">Life Coach</p>
    </div>
    <ul class="contacts">
      <li class="contacts__item">
        <svg class="contacts__icon" viewBox="0 0 22 22" aria-hidden="true">
          <circle cx="11" cy="11" r="11" fill="#fff"/>
          <path d="M7.5 5.5l2 2.6-1.2 1.4c.8 1.7 2 2.9 3.7 3.7l1.4-1.2 2.6 2-1.2 2c-4.6-.5-8.3-4.2-8.8-8.8z" fill="var(--wine)"/>
        </svg>
        <span>518.677.3941</span>
      </li>
      <li class="contacts__item">
        <svg class="contacts__icon" viewBox="0 0 22 22" aria-hidden="true">
          <circle cx="11" cy="11" r="11" fill="#fff"/>
          <rect x="5.5" y="7" width="11" height="8" fill="none" stroke="var(--wine)" stroke-width="1.3"/>
          <path d="M5.5 7l5.5 4.5L16.5 7" fill="none" stroke="var(--wine)" stroke-width="1.3"/>
        </svg>
        <span>marissa@calmbriefcounsel.net</span>
      </li>
      <li class="contacts__item">
        <svg class="contacts__icon" viewBox="0 0 22 22" aria-hidden="true">
          <circle cx="11" cy="11" r="11" fill="#fff"/>
          <circle cx="11" cy="11" r="5.5" fill="none" stroke="var(--wine)" stroke-width="1.3"/>
          <ellipse cx="11" cy="11" rx="2.3" ry="5.5" fill="none" stroke="var(--wine)" stroke-width="1.1"/>
          <path d="M5.5 11h11" stroke="var(--wine)" stroke-width="1.1"/>
        </svg>
        <span>www.calmbriefcounsel.net</span>
      </li>
      <li class="contacts__item">
        <svg class="contacts__icon" viewBox="0 0 22 22" aria-hidden="true">
          <circle cx="11" cy="11" r="11" fill="#fff"/>
        </svg>
        <span>@calmbriefcounsel</span>
      </li>
    </ul>
  </section>
</main>
</body>
</html>
```